Cash Flow Slide Design

Help Make Slide flow, FT Arrow to paying Down HELOC Then Bring in new Home Purchase and look amazing.
Serif
EB3D1F
EC4F4E
F09395
F8D3D4
FCEDEE

```html
<!DOCTYPE html>
<html lang="en">
<head>
<meta charset="utf-8">
<title>Wealth Builder Account – Cash Flow Slide</title>
<link rel="stylesheet" href="https://fonts.googleapis.com/css2?family=Lato:wght@400;700;900&display=swap">
<style>
  :root {
    --page: #000000;
    --slide: #121212;
    --header-band: #0b0b0b;
    --red: #eb3d1f;
    --red-deep: #d81b1b;
    --red-soft: #ec4f4e;
    --column-dark: #5a1414;
    --pink: #f09395;
    --blush: #f8d3d4;
    --mist: #fcedee;
    --white: #ffffff;
    --grey: #a9a9a9;
    --line: #6a6a6a;
  }
  html, body {
    margin: 0;
    padding: 0;
    width: 884px;
    height: 1200px;
    overflow: hidden;
    background: var(--page);
  }
  .canvas {
    position: relative;
    width: 884px;
    height: 1200px;
    background: var(--page);
  }
  .slide {
    position: absolute;
    left: 0;
    top: 352px;
    width: 884px;
    height: 496px;
    display: block;
    font-family: "Lato", sans-serif;
  }
  .slide text { font-family: "Lato", sans-serif; }
  .brand-name { fill: var(--white); font-weight: 900; font-size: 52px; letter-spacing: 1px; }
  .slide-title { fill: var(--red-deep); font-weight: 700; font-size: 46px; }
  .step-label { fill: var(--white); font-weight: 700; font-size: 30px; }
  .flow-note { fill: var(--white); font-weight: 400; font-size: 17px; }
  .column-note { fill: var(--white); font-weight: 700; font-size: 18px; }
  .column-small { fill: var(--white); font-weight: 400; font-size: 12.5px; }
  .offset-caption { fill: var(--grey); font-weight: 700; font-size: 28px; }
  .icon-stroke { fill: none; stroke: #222; stroke-width: 3; stroke-linecap: round; stroke-linejoin: round; }
</style>
</head>
<body>
<main class="canvas">
  <svg class="slide" viewBox="0 0 1568 880" xmlns="http://www.w3.org/2000/svg" aria-label="Wealth Builder Account cash flow slide">
    <defs>
      <linearGradient id="title-rule" x1="0" x2="1">
        <stop offset="0" stop-color="#555" stop-opacity="0"/>
        <stop offset="0.5" stop-color="#777"/>
        <stop offset="1" stop-color="#555" stop-opacity="0"/>
      </linearGradient>
      <linearGradient id="house-fill" x1="0" y1="0" x2="0" y2="1">
        <stop offset="0" stop-color="#ec4f4e"/>
        <stop offset="0.35" stop-color="#f8d3d4"/>
        <stop offset="1" stop-color="#fcedee"/>
      </linearGradient>
      <marker id="arrow-head" viewBox="0 0 12 12" refX="10" refY="6" markerWidth="10" markerHeight="10" orient="auto">
        <path d="M1 1 L10 6 L1 11" fill="none" stroke="#d81b1b" stroke-width="2"/>
      </marker>
      <marker id="arrow-thin" viewBox="0 0 12 12" refX="10" refY="6" markerWidth="12" markerHeight="12" orient="auto">
        <path d="M1 2 L10 6 L1 10" fill="none" stroke="#d81b1b" stroke-width="1"/>
      </marker>
    </defs>

    <!-- background and header -->
    <rect class="slide-bg" width="1568" height="880" fill="var(--slide)"/>
    <rect class="header-band" x="176" y="0" width="1392" height="127" fill="var(--header-band)"/>

    <!-- brand -->
    <g class="brand">
      <circle cx="570" cy="62" r="30" fill="var(--red-deep)"/>
      <text class="brand-name" x="615" y="82">NORTHVALE FINANCIAL</text>
    </g>

    <!-- title -->
    <text class="slide-title" x="745" y="172" text-anchor="middle">Wealth Builder Account</text>
    <rect class="title-rule" x="520" y="190" width="440" height="2" fill="url(#title-rule)"/>

    <!-- columns -->
    <g class="column column-checking">
      <rect x="163" y="216" width="87" height="430" rx="43.5" fill="var(--column-dark)"/>
      <path d="M163 554 a43.5 43.5 0 0 1 87 0 V646 H163 Z" fill="var(--red-deep)"/>
      <text class="column-note" x="206" y="551" text-anchor="middle">Minimum</text>
      <text class="column-note" x="206" y="572" text-anchor="middle">Reserve</text>
    </g>

    <g class="column column-insurance">
      <rect x="461" y="216" width="88" height="430" rx="44" fill="var(--column-dark)"/>
      <path d="M461 332 a44 44 0 0 1 88 0 V646 H461 Z" fill="var(--red-deep)"/>
      <path d="M461 505 a44 44 0 0 1 88 0 V646 H461 Z" fill="#c8181a"/>
      <text class="column-small" x="505" y="257" text-anchor="middle">Optimal</text>
      <text class="column-small" x="505" y="271" text-anchor="middle">Transfer Point</text>
      <text class="column-small" x="505" y="338" text-anchor="middle">Cash Value</text>
      <text class="column-small" x="505" y="351" text-anchor="middle">Continues</text>
      <text class="column-small" x="505" y="364" text-anchor="middle">To Grow</text>
      <text class="column-small" x="505" y="413" text-anchor="middle">Can never</text>
      <text class="column-small" x="505" y="426" text-anchor="middle">lose</text>
      <text class="column-small" x="505" y="439" text-anchor="middle">Principal</text>
      <text class="column-note" x="505" y="551" text-anchor="middle">Cash</text>
      <text class="column-note" x="505" y="572" text-anchor="middle">Value</text>
    </g>

    <g class="column column-heloc">
      <rect x="763" y="216" width="87" height="430" rx="43.5" fill="var(--column-dark)"/>
    </g>

    <!-- step badges -->
    <g class="badge badge-checking">
      <circle cx="206" cy="646" r="64" fill="none" stroke="var(--red-deep)" stroke-width="2"/>
      <circle cx="206" cy="646" r="58" fill="var(--red-deep)"/>
      <circle cx="206" cy="646" r="38" fill="var(--white)"/>
      <circle class="icon-stroke" cx="206" cy="646" r="20"/>
      <path class="icon-stroke" d="M196 646 l7 8 l16 -20"/>
    </g>
    <g class="badge badge-insurance">
      <circle cx="505" cy="646" r="64" fill="none" stroke="var(--red-deep)" stroke-width="2"/>
      <circle cx="505" cy="646" r="58" fill="var(--red-deep)"/>
      <circle cx="505" cy="646" r="38" fill="var(--white)"/>
      <path class="icon-stroke" d="M505 626 l14 6 v10 c0 10 -7 16 -14 19 c-7 -3 -14 -9 -14 -19 v-10 Z"/>
      <path class="icon-stroke" d="M499 643 l4 5 l8 -9"/>
    </g>
    <g class="badge badge-heloc">
      <circle cx="805" cy="646" r="64" fill="none" stroke="var(--red-deep)" stroke-width="2"/>
      <circle cx="805" cy="646" r="58" fill="var(--red-deep)"/>
      <circle cx="805" cy="646" r="38" fill="var(--white)"/>
      <path class="icon-stroke" d="M785 648 l20 -20 l20 20 M790 643 v22 h30 v-22 M800 665 v-12 h10 v12"/>
    </g>

    <!-- flow arrows -->
    <g class="flow-arrows" stroke="var(--red-deep)" stroke-width="4" fill="none">
      <line x1="272" y1="646" x2="402" y2="646" marker-end="url(#arrow-head)"/>
      <line x1="571" y1="646" x2="707" y2="646" marker-end="url(#arrow-head)"/>
      <line x1="871" y1="646" x2="1002" y2="646" marker-end="url(#arrow-head)"/>
    </g>

    <!-- flow notes -->
    <g class="flow-notes">
      <text class="flow-note" x="91" y="555" text-anchor="middle">Income</text>
      <line x1="48" y1="580" x2="148" y2="580" stroke="var(--red-deep)" stroke-width="1" marker-end="url(#arrow-thin)"/>
      <text class="flow-note" x="394" y="508" text-anchor="middle">Funds</text>
      <text class="flow-note" x="394" y="528" text-anchor="middle">Transfer</text>
      <line x1="352" y1="534" x2="452" y2="534" stroke="var(--red-deep)" stroke-width="1" marker-end="url(#arrow-thin)"/>
      <text class="flow-note" x="670" y="426" text-anchor="middle">Funds</text>
      <text class="flow-note" x="671" y="446" text-anchor="middle">Transfer</text>
      <line x1="628" y1="452" x2="728" y2="452" stroke="var(--red-deep)" stroke-width="1" marker-end="url(#arrow-thin)"/>
      <text class="flow-note" x="935" y="367" text-anchor="middle">New Home</text>
      <text class="flow-note" x="935" y="387" text-anchor="middle">Purchase</text>
      <line x1="893" y1="392" x2="993" y2="392" stroke="var(--red-deep)" stroke-width="1" marker-end="url(#arrow-thin)"/>
    </g>

    <!-- house illustration area -->
    <rect class="house-illustration" x="1012" y="232" width="416" height="432" rx="10" fill="url(#house-fill)" role="img" aria-label="Illustration of a white house with a red roof and red door, representing the new home purchase"/>

    <!-- step labels -->
    <text class="step-label" x="218" y="746" text-anchor="middle">Checking</text>
    <text class="step-label" x="511" y="744" text-anchor="middle">OA Life Insurance</text>
    <text class="step-label" x="805" y="742" text-anchor="middle">HELOC</text>
    <text class="step-label" x="1245" y="741" text-anchor="middle">New Home Purchase</text>

    <!-- timeline -->
    <g class="timeline">
      <line x1="100" y1="774" x2="1408" y2="774" stroke="var(--line)" stroke-width="1.5" stroke-dasharray="5 4"/>
      <circle cx="100" cy="774" r="4" fill="var(--line)"/>
      <circle cx="1408" cy="774" r="4" fill="var(--line)"/>
      <g fill="var(--white)">
        <circle cx="208" cy="774" r="17"/>
        <circle cx="502" cy="774" r="17"/>
        <circle cx="804" cy="774" r="17"/>
        <circle cx="1235" cy="774" r="17"/>
      </g>
      <g fill="var(--red-deep)">
        <circle cx="208" cy="774" r="10"/>
        <circle cx="502" cy="774" r="10"/>
        <circle cx="804" cy="774" r="10"/>
        <circle cx="1235" cy="774" r="10"/>
      </g>
    </g>

    <text class="offset-caption" x="784" y="831" text-anchor="middle">Offset Account: Permanent Life Insurance</text>
  </svg>
</main>
</body>
</html>
```